Design Tweak needed for a current site

Design on top of an existing quiz funnel

Ideally we would like to tweak what we have already built here (moving elements, styles, adding simple elements etc): http://offers.rateplumfinder.com/could-you-cut-your-auto-premium

The flow:
1) User lands on the quiz page
2) User answers X questions and moves through the flow
3) Calculating user results screen
4) User reaches a success screen, and is subsequently redirected

Keys to the design:
1) We need to emphasize the quiz title as that will drive engagement. In this case, this is a quiz to see if you might be eligible to save money on car insurance.

2) At the end of the quiz we need to make it very, very clear that the user is eligible for savings and that in order to complete the process they are being redirected to another page where they need to fill out a form. It is critical that the design communicates this very clearly... We can count down the time left until redirect and we can use any order of elements to make this point. I think our current design does a very bad job of this.

3) We want to have a "calculating" step so that it seems like the page is working in the background

Goals of the design:
1) Polished, high quality experience throughout
2) User is clearly prepared to be redirected to the conversion funnel/landing page at the end
3) User understands the value of completing the quiz

Target Market(s)

designers

Industry/Entity Type

Moving

Number of Pages Required

1 page

Font styles to use
Sans Serif

Colors

Designer to choose colors to be used in the design.

Requirements
Must have
• This quiz funnel is a template so while the current use case is for auto insurance, we would like a design that also would work in other contexts.
Should not have
• We don't want to materially change the core functionality of the quiz itself... redesigning any of the elements or interactions is encouraged though

```html
<!DOCTYPE html>
<html lang="en">
<head>
<meta charset="utf-8">
<title>RatePlumFinder – Car Insurance Quiz</title>
<link rel="stylesheet" href="https://fonts.googleapis.com/css2?family=Play:wght@400;700&family=Open+Sans:wght@400&display=swap">
<style>
  :root {
    --brand-blue: #1784aa;
    --footer-dark: #232323;
    --teal: #56bfc1;
    --stripe-light: #58c0cf;
    --stripe-dark: #3b8e9d;
    --track: #dedede;
    --panel-grey: #f4f4f4;
    --ink: #333333;
    --white: #ffffff;
  }
  * { box-sizing: border-box; margin: 0; padding: 0; }
  html, body {
    width: 1200px; height: 849px; overflow: hidden;
    background: var(--footer-dark);
    font-family: "Play", sans-serif; color: var(--ink);
  }
  .page { position: relative; width: 1200px; height: 849px; }

  .site-header {
    position: absolute; top: 0; left: 0; width: 1200px; height: 107px;
    background: var(--white);
    display: flex; align-items: center; justify-content: center; gap: 10px;
  }
  .brand-dot { width: 42px; height: 42px; border-radius: 50%; background: var(--brand-blue); }
  .brand-name { font-size: 37px; font-weight: 400; color: #1a1a1a; letter-spacing: 0.5px; }

  .hero-band {
    position: absolute; top: 107px; left: 0; width: 1200px; height: 529px;
    background: var(--brand-blue);
  }

  .quiz-card {
    position: absolute; top: 149px; left: 89px; width: 1024px; height: 624px;
    background: var(--white); border-radius: 4px; overflow: hidden;
  }
  .quiz-intro {
    height: 144px; background: var(--panel-grey); text-align: center; padding-top: 39px;
  }
  .quiz-title { font-size: 27px; font-weight: 400; letter-spacing: 0.4px; }
  .quiz-subtitle { margin-top: 10px; font-size: 16.5px; letter-spacing: 0.2px; }

  .step-track { position: absolute; top: 218px; left: 274px; width: 472px; height: 40px; }
  .step-line { position: absolute; top: 18px; left: 20px; width: 432px; height: 3px; background: var(--teal); }
  .step {
    position: absolute; top: 0; width: 40px; height: 40px; border-radius: 50%;
    background: var(--teal); color: var(--white);
    font-size: 20px; line-height: 40px; text-align: center;
  }

  .calc-heading {
    position: absolute; top: 330px; left: 0; width: 100%; text-align: center;
    font-size: 25px; letter-spacing: 0.3px;
  }
  .progress {
    position: absolute; top: 390px; left: 272px; width: 480px; height: 16px;
    background: var(--track); border-radius: 8px; overflow: hidden;
  }
  .progress-fill {
    width: 347px; height: 100%; border-radius: 8px;
    background: repeating-linear-gradient(-45deg,
      var(--stripe-light) 0 8px, var(--stripe-dark) 8px 12px);
  }
  .calc-note {
    position: absolute; top: 433px; left: 0; width: 100%; text-align: center;
    font-size: 15.5px; letter-spacing: 0.2px;
  }

  .site-footer {
    position: absolute; top: 800px; left: 0; width: 1200px; text-align: center;
    font-family: "Open Sans", sans-serif; font-size: 12.5px; color: var(--white);
  }
  .build-tag {
    position: absolute; top: 797px; left: 1163px;
    font-family: "Open Sans", sans-serif; font-size: 12px; color: var(--white);
  }
</style>
</head>
<body>
<div class="page">
  <header class="site-header">
    <span class="brand-dot"></span>
    <span class="brand-name">RatePlumFinder</span>
  </header>

  <div class="hero-band"></div>

  <main class="quiz-card">
    <section class="quiz-intro">
      <h1 class="quiz-title">Quiz: Are You Overpaying For Car Insurance?</h1>
      <p class="quiz-subtitle">Take our five question quiz to see if you might be eligible for car insurance savings</p>
    </section>

    <div class="step-track" aria-label="Quiz progress: all five steps complete">
      <div class="step-line"></div>
      <div class="step" style="left:0">1</div>
      <div class="step" style="left:102px">2</div>
      <div class="step" style="left:205px">3</div>
      <div class="step" style="left:308px">4</div>
      <div class="step" style="left:412px">5</div>
    </div>

    <h2 class="calc-heading">Calculating Your Potential Savings...</h2>
    <div class="progress" role="progressbar" aria-valuenow="72" aria-valuemin="0" aria-valuemax="100">
      <div class="progress-fill"></div>
    </div>
    <p class="calc-note">Hang tight! We're reviewing your answers and looking for savings.</p>
  </main>

  <footer class="site-footer">Copyright © 2017. All Rights Reserved</footer>
  <span class="build-tag">C6</span>
</div>
</body>
</html>
```